Creative - Appealing - Business Card Design Project

Looking for a Business card design (vector artwork) for an existing company called 'Fernway Sound'. We operate in the entertainment industry specializing in audio system design and rental, however; we also deal with other sectors of the entertainment industry including lighting, video, staging and power system design and rental. We would like to see designs that don't focus too much on audio but include elements encompassing everything else.

Double sided business card, following our new colour scheme and logo, which is attached. The card would ideally be creative and eye catching to draw in new customers in the elegant event production market, such as weddings & corporate affairs.

Target Market(s)

High end corporate clients, wedding clients

Industry/Entity Type

Entertainment

Requirements
Must have
• Our contact details, these can be worded & listed however you think appropriate as part as the design

Business Name - Fernway Sound
My Name - Dominic Harwell
Web Address - www.fernwaysound-example.com
Mobile Number - 07914 362 517
Office Number - 0330 481 7265
Email - dom@fernwaysound-example.com

The name, email and mobile number would need to be able to be changed to my business partners also.

The font used on our logo is Sansation
Nice to have
• On one side maybe a word cloud involving the services in which we can provide; Lighting, Sound, Event Production, Staging, LED Uplighting, Projection Mapping, Wedding Hire

On the other side, all the important credentials of contact.
Should not have
• The design should not use any old style fonts (i.e Times New Roman, Gothic etc) or on the other side of the scale, any 'jokey' fonts (i.e. Comic Sans).

The font to be used is Sansation

```html
<!DOCTYPE html>
<html lang="en">
<head>
<meta charset="utf-8">
<title>Fernway Sound – Business Card Set</title>
<link rel="stylesheet" href="https://fonts.googleapis.com/css2?family=Sansation:wght@400;700&display=swap">
<style>
  :root {
    --stage: #e8e5e1;
    --card: #ffffff;
    --ink: #2b2b2b;
    --ink-soft: #3a3a3a;
    --grey: #8f8f8f;
    --purple: #4f3a88;
    --purple-deep: #2f2a5c;
    --purple-mid: #6a4f9f;
    --purple-light: #a595ca;
    --white: #ffffff;
  }
  * { margin: 0; padding: 0; box-sizing: border-box; }
  html, body { width: 1200px; height: 800px; overflow: hidden; }
  body {
    background: var(--stage);
    font-family: "Sansation", sans-serif;
    color: var(--ink);
    position: relative;
  }
  .side-label {
    position: absolute;
    width: 510px;
    text-align: center;
    font-size: 22px;
    font-weight: 400;
    color: var(--ink);
  }
  .card {
    position: absolute;
    width: 510px;
    height: 290px;
    border-radius: 22px;
    background: var(--card);
    overflow: hidden;
    box-shadow: 0 4px 10px rgba(0,0,0,0.18);
  }
  .card--front { left: 68px; top: 92px; }
  .card--back-1 { left: 621px; top: 90px; }
  .card--back-2 { left: 70px; top: 450px; }
  .card--back-3 {
    left: 621px; top: 450px;
    background: linear-gradient(90deg, var(--purple-deep) 0%, var(--purple-mid) 70%, var(--purple-light) 100%);
  }

  /* brand name setting */
  .brand {
    position: absolute;
    text-align: center;
    font-weight: 700;
    color: var(--purple);
    line-height: 1;
  }
  .brand__mark {
    display: block;
    margin: 0 auto;
    background: var(--purple);
  }
  .brand__name { display: block; }

  /* front */
  .front-brand { left: 28px; top: 44px; width: 250px; }
  .front-brand .brand__mark { width: 70px; height: 70px; margin-bottom: 32px; }
  .front-brand .brand__name { font-size: 33px; letter-spacing: 0.5px; }
  .front-brand .brand__name + .brand__name { font-size: 22px; margin-top: 6px; }

  .divider {
    position: absolute; left: 267px; top: 36px;
    width: 2px; height: 190px;
    background: linear-gradient(180deg, rgba(150,150,150,0) 0%, #9a9a9a 50%, rgba(150,150,150,0) 100%);
  }
  .holder-name {
    position: absolute; left: 299px; top: 73px;
    font-size: 17px; font-weight: 700; color: var(--ink-soft);
  }
  .phones {
    position: absolute; left: 299px; top: 152px;
    list-style: none; font-size: 13px; line-height: 21px; color: var(--ink);
  }
  .phones b, .online b { font-weight: 700; }
  .front-bands { position: absolute; left: 0; bottom: 0; width: 510px; height: 56px; }
  .online {
    position: absolute; left: 296px; top: 244px;
    list-style: none; font-size: 12px; line-height: 18px; color: var(--white);
    white-space: nowrap;
  }

  /* shared services */
  .services-title {
    font-size: 15px; font-weight: 700; color: var(--purple);
  }
  .service {
    display: inline-block;
    font-size: 15px; color: var(--grey);
    white-space: nowrap;
  }
  .service::before {
    content: "";
    display: inline-block;
    width: 0; height: 0;
    border-left: 4px solid transparent;
    border-right: 4px solid transparent;
    border-bottom: 8px solid currentColor;
    margin-right: 3px;
    vertical-align: 1px;
  }
  .web {
    position: absolute; left: 0; width: 100%;
    text-align: center; font-size: 13px; letter-spacing: 2px; color: var(--ink);
  }

  /* back 1 */
  .back1-brand { left: 0; top: 18px; width: 100%; }
  .back1-brand .brand__mark { width: 56px; height: 56px; margin-bottom: 24px; }
  .back1-brand .brand__name { font-size: 27px; }
  .back1-brand .brand__name + .brand__name { font-size: 18px; margin-top: 4px; }
  .back1-services {
    position: absolute; left: 0; top: 178px; width: 100%; text-align: center;
  }
  .back1-services .service-row { margin-top: 6px; line-height: 18px; }
  .back1-services .service { margin: 0 2px; }
  .card--back-1 .web { top: 258px; }

  /* back 2 */
  .back2-brand { left: 34px; top: 70px; width: 220px; }
  .back2-brand .brand__mark { width: 80px; height: 80px; margin-bottom: 26px; }
  .back2-brand .brand__name { font-size: 30px; }
  .back2-brand .brand__name + .brand__name { margin-top: 6px; }
  .back2-services { position: absolute; left: 284px; top: 45px; }
  .back2-services ul { list-style: none; margin-top: 4px; }
  .back2-services li { display: block; line-height: 23.5px; }
  .back2-services .service::before { margin-right: 8px; }
  .card--back-2 .web { top: 261px; }

  /* back 3 */
  .back3-services {
    position: absolute; left: 0; top: 56px; width: 100%; text-align: center; color: var(--white);
  }
  .back3-services .services-title { color: var(--white); }
  .back3-services .service { color: var(--white); margin: 0 1px; }
  .back3-services .service-row { line-height: 33.5px; }
  .back3-services .services-title + .service-row { margin-top: 8px; }
  .card--back-3 .web { top: 258px; color: var(--white); }
</style>
</head>
<body>

  <h2 class="side-label" style="left:68px; top:50px;">Front</h2>
  <h2 class="side-label" style="left:621px; top:50px;">Back - 1</h2>
  <h2 class="side-label" style="left:70px; top:410px;">Back - 2</h2>
  <h2 class="side-label" style="left:621px; top:410px;">Back - 3</h2>

  <section class="card card--front">
    <div class="brand front-brand">
      <span class="brand__mark"></span>
      <span class="brand__name">FERNWAY</span>
      <span class="brand__name">SOUND</span>
    </div>
    <div class="divider"></div>
    <p class="holder-name">Dominic Harwell</p>
    <ul class="phones">
      <li><b>c</b> : 07914 362 517</li>
      <li><b>p</b> : 0330 481 7265</li>
    </ul>
    <svg class="front-bands" viewBox="0 0 510 56" aria-hidden="true">
      <defs>
        <linearGradient id="bandPurple" x1="0" x2="1" y1="0" y2="0">
          <stop offset="0" stop-color="#4a3a86"/>
          <stop offset="1" stop-color="#7d65b0"/>
        </linearGradient>
      </defs>
      <polygon points="0,28 265,28 255,40 0,40" fill="#9a9a9a"/>
      <polygon points="264,44 297,4 510,4 510,56 0,56 0,44" fill="url(#bandPurple)"/>
    </svg>
    <ul class="online">
      <li><b>e</b> : dom@fernwaysound-example.com</li>
      <li><b>w</b> : www.fernwaysound-example.com</li>
    </ul>
  </section>

  <section class="card card--back-1">
    <div class="brand back1-brand">
      <span class="brand__mark"></span>
      <span class="brand__name">FERNWAY</span>
      <span class="brand__name">SOUND</span>
    </div>
    <div class="back1-services">
      <p class="services-title">WE CAN PROVIDE</p>
      <p class="service-row">
        <span class="service">Lighting</span>
        <span class="service">Sound</span>
        <span class="service">Event Production</span>
        <span class="service">Staging</span>
      </p>
      <p class="service-row">
        <span class="service">LED Uplighting</span>
        <span class="service">Projection Mapping</span>
        <span class="service">Wedding Hire</span>
      </p>
    </div>
    <p class="web">www.fernwaysound-example.com</p>
  </section>

  <section class="card card--back-2">
    <div class="brand back2-brand">
      <span class="brand__mark"></span>
      <span class="brand__name">FERNWAY</span>
      <span class="brand__name">SOUND</span>
    </div>
    <div class="back2-services">
      <p class="services-title">WE CAN PROVIDE</p>
      <ul>
        <li class="service">Lighting</li>
        <li class="service">Sound</li>
        <li class="service">Event Production</li>
        <li class="service">Staging</li>
        <li class="service">LED Uplighting</li>
        <li class="service">Projection Mapping</li>
        <li class="service">Wedding Hire</li>
      </ul>
    </div>
    <p class="web">www.fernwaysound-example.com</p>
  </section>

  <section class="card card--back-3">
    <div class="back3-services">
      <p class="services-title">WE CAN PROVIDE</p>
      <p class="service-row">
        <span class="service">Lighting</span>
        <span class="service">Sound</span>
      </p>
      <p class="service-row">
        <span class="service">Event Production</span>
        <span class="service">Staging</span>
      </p>
      <p class="service-row">
        <span class="service">LED Uplighting</span>
        <span class="service">Projection Mapping</span>
      </p>
      <p class="service-row">
        <span class="service">Wedding Hire</span>
      </p>
    </div>
    <p class="web">www.fernwaysound-example.com</p>
  </section>

</body>
</html>
```